Amber Meadow LLC business card

I help with the Marketing and Sales of various Natural, Organic, Eco Friendly and Healthy Main Stream products to Retail Corporate accounts as well as Independents and Distributors.I also highlight Private label items to these same Retail Corporate accounts.Cherish the Moments, Enjoy Life!

Speciality & Health Sales and Marketing

Target Market(s)

Men and Women

Industry/Entity Type

Business

Contact Information for Business Card

Amber Meadow, LLC
Lydia Rose Vandermeer
427 West Orchard Lane
Ste 5-384
Phoenix, AZ 85317
602-718-3054
lvandermeer@pinemail.net

Requirements
Must have
• Nice, femine font
Something in the background or on a side with a softness
Nice to have
• Cherish the Moments, Enjoy Life
Should not have
• Hardness

```html
<!DOCTYPE html>
<html lang="en">
<head>
<meta charset="utf-8">
<title>Amber Meadow LLC — Business Card</title>
<link rel="stylesheet" href="https://fonts.googleapis.com/css2?family=Dancing+Script:wght@500&family=Noto+Serif:ital,wght@0,400;1,400&display=swap">
<style>
  :root {
    --page: #e9e9e9;
    --card: #f8f7dd;
    --green: #5cb87a;
    --green-soft: #a9d8b3;
    --green-pale: #d5ebcd;
    --shadow: rgba(0, 0, 0, 0.18);
  }
  * { margin: 0; padding: 0; box-sizing: border-box; }
  html, body {
    width: 1200px;
    height: 1127px;
    overflow: hidden;
    background: var(--page);
  }
  .card {
    position: absolute;
    left: 100px;
    top: 271px;
    width: 1000px;
    height: 584px;
    background: var(--card);
    box-shadow: 0 3px 8px var(--shadow);
    color: var(--green);
  }
  .card__pattern {
    position: absolute;
    left: 0;
    top: 0;
    width: 380px;
    height: 100%;
    background: linear-gradient(160deg, var(--green-pale) 0%, var(--card) 55%, var(--green-pale) 100%);
  }
  .card__heading {
    position: absolute;
    right: 53px;
    top: 75px;
    text-align: right;
  }
  .card__name {
    font-family: "Dancing Script", cursive;
    font-weight: 500;
    font-size: 50px;
    line-height: 1;
  }
  .card__company {
    font-family: "Noto Serif", serif;
    font-style: italic;
    font-size: 28px;
    line-height: 1.2;
  }
  .contact {
    position: absolute;
    left: 440px;
    list-style: none;
    font-family: "Noto Serif", serif;
    font-size: 32px;
    line-height: 41px;
  }
  .contact__item {
    position: absolute;
    left: 0;
    display: flex;
    align-items: center;
    white-space: nowrap;
  }
  .contact__icon {
    width: 34px;
    height: 34px;
    margin-right: 24px;
    fill: none;
    stroke: var(--green);
    stroke-width: 2;
    flex: none;
  }
  .contact__item--address { top: 225px; }
  .contact__item--phone { top: 385px; }
  .contact__item--email { top: 467px; }
</style>
</head>
<body>
  <article class="card">
    <div class="card__pattern" role="img" aria-label="Soft repeating pattern of pale green flowers on a faint diagonal lattice"></div>

    <header class="card__heading">
      <h1 class="card__name">Lydia Rose Vandermeer</h1>
      <p class="card__company">Amber Meadow, LLC</p>
    </header>

    <ul class="contact">
      <li class="contact__item contact__item--address">
        <svg class="contact__icon" viewBox="0 0 24 24" aria-hidden="true">
          <path d="M12 21s-6-6.2-6-11a6 6 0 0 1 12 0c0 4.8-6 11-6 11z"/>
          <circle cx="12" cy="10" r="2.2"/>
        </svg>
        <span>427 West Orchard Lane<br>Ste 5-384 Phoenix,<br>AZ 85317</span>
      </li>
      <li class="contact__item contact__item--phone">
        <svg class="contact__icon" viewBox="0 0 24 24" aria-hidden="true">
          <path d="M7 3l3 4-2 2c1 2.5 3 4.5 5.5 5.5l2-2 4 3-2 3.5C10 18 5 13 3.5 5.5z"/>
        </svg>
        <span>602-718-3054</span>
      </li>
      <li class="contact__item contact__item--email">
        <svg class="contact__icon" viewBox="0 0 24 24" aria-hidden="true">
          <rect x="2.5" y="5.5" width="19" height="13"/>
          <path d="M2.5 5.5l9.5 7.5 9.5-7.5M2.5 18.5l7-6.5M21.5 18.5l-7-6.5"/>
        </svg>
        <span>lvandermeer@pinemail.net</span>
      </li>
    </ul>
  </article>
</body>
</html>
```